Estate Agent/Real Estate valuation tool

We need a design for our our new estate agent valuation tool.

The tool allows users to book a valuation of their house/property with the estate agent, after they choose there property they can then complete their details and choose a booking time.

The mock up of the design we want is attached to this project.(Main Screen)

This also needs to be responsive so the design is easy to use on a mobile device.

Target Market(s)

estate agents

Industry/Entity Type

Real Estate Agent

Number of Pages Required

1 page

Requirements
Must have
• Section 2 and 3 greyed out when user is on step 1
• Section 1 and 3 greyed out when user is on step 2
• Section 1 and 2 greyed out when the user is on step 3
• *** Design must be shown for mobile/ipad and desktop
Nice to have
• Clean and Simple
Should not have
• Dark colours

```html
<!DOCTYPE html>
<html lang="en">
<head>
<meta charset="utf-8">
<title>Book your Valuation Online</title>
<link rel="stylesheet" href="https://fonts.googleapis.com/css2?family=Cinzel:wght@400;600&family=Open+Sans:wght@400;600&display=swap">
<style>
  :root {
    --sky-top: #3f6fc4;
    --sky-mid: #a9c3e3;
    --stone-light: #d9d9d9;
    --stone-mid: #9a9a9a;
    --stone-dark: #4a4a4a;
    --brand-blue: #2f74bd;
    --field-blue: #3c7ab9;
    --field-grey: #a9a9a9;
    --card-top: #f2f2f2;
    --card-bottom: #c9c9c9;
    --rule: #9c9c9c;
    --ink: #1a1a1a;
    --ink-soft: #2c2c2c;
    --white: #ffffff;
    --btn-light: #2a86d2;
    --btn-dark: #1f4562;
    --chip: #a3a3a3;
    --search: #222222;
  }
  * { box-sizing: border-box; margin: 0; padding: 0; }
  html, body { width: 1200px; height: 797px; overflow: hidden; }
  body { font-family: "Open Sans", Arial, sans-serif; color: var(--ink); }

  .page { position: relative; width: 1200px; height: 797px; overflow: hidden; }

  .backdrop {
    position: absolute; inset: 0;
    background:
      radial-gradient(ellipse 40% 30% at 45% 12%, rgba(255,255,255,0.75), transparent 70%),
      linear-gradient(160deg, var(--sky-top) 0%, var(--sky-mid) 18%, var(--stone-light) 38%, var(--stone-mid) 62%, var(--stone-dark) 100%);
  }

  .brand {
    position: absolute; left: 529px; top: 36px; width: 142px; height: 58px;
    background: var(--brand-blue); border-radius: 5px;
    color: var(--white); font-family: "Cinzel", Georgia, serif; font-size: 26px;
    display: flex; align-items: center; justify-content: center;
  }

  .headline {
    position: absolute; left: 0; right: 0; top: 170px; text-align: center;
    font-family: "Cinzel", Georgia, serif; font-weight: 400; font-size: 40px;
    letter-spacing: 2px; color: #0b0b0b;
  }

  .step {
    position: absolute; top: 316px; width: 305px; height: 348px;
    border-radius: 8px; overflow: visible;
    background: linear-gradient(180deg, var(--card-top), var(--card-bottom));
    box-shadow: 0 4px 14px rgba(0,0,0,0.35);
  }
  .step--property { left: 68px; }
  .step--details { left: 443px; }
  .step--time { left: 818px; }

  .step-tag {
    position: absolute; top: -26px; left: 100px; width: 105px; height: 26px;
    background: var(--brand-blue); border-radius: 4px 4px 0 0;
    color: var(--white); font-size: 12px; letter-spacing: 0.5px;
    display: flex; align-items: center; justify-content: center;
  }

  .step-title {
    height: 44px; border-bottom: 1px solid var(--rule);
    font-family: "Cinzel", Georgia, serif; font-size: 19px; letter-spacing: 1.5px;
    display: flex; align-items: center; justify-content: center; color: var(--ink);
  }

  .step-body { position: absolute; inset: 44px 0 56px 0; }

  .field-label {
    position: absolute; left: 25px; font-size: 14px; letter-spacing: 0.4px; color: var(--ink-soft);
  }
  .field-input {
    position: absolute; left: 23px; width: 259px; height: 30px;
    background: var(--field-blue); border-radius: 2px;
  }
  .field-input--short { width: 188px; }
  .search-btn {
    position: absolute; left: 215px; width: 67px; height: 30px; border-radius: 3px;
    background: var(--search); color: var(--white); font-size: 13px; letter-spacing: 0.5px;
    display: flex; align-items: center; justify-content: center;
  }
  .field-filled {
    position: absolute; left: 23px; width: 259px; height: 30px; padding-left: 10px;
    background: var(--field-grey); border-radius: 2px;
    font-size: 14px; letter-spacing: 0.5px; display: flex; align-items: center; color: var(--ink);
  }

  .day-toggle {
    position: absolute; top: 25px; height: 22px; font-size: 13px; letter-spacing: 0.5px;
    display: flex; align-items: center; justify-content: center; background: var(--chip);
  }
  .day-toggle--today { left: 23px; width: 127px; }
  .day-toggle--tomorrow { left: 156px; width: 127px; background: var(--field-blue); color: var(--white); }

  .chip-row { position: absolute; left: 23px; display: flex; gap: 6px; }
  .chip {
    width: 47px; height: 38px; background: var(--chip); border-radius: 2px;
    font-size: 12px; line-height: 1.25; text-align: center;
    display: flex; align-items: center; justify-content: center; color: var(--ink);
  }
  .chip--selected { background: var(--field-blue); color: var(--white); }
  .chip-row--days { top: 53px; }
  .chip-row--times { top: 179px; }

  .date-display {
    position: absolute; left: 22px; top: 118px; width: 262px; height: 32px;
    border: 1px solid #8c8c8c; border-radius: 2px; background: rgba(255,255,255,0.35);
    font-size: 15px; letter-spacing: 0.4px; display: flex; align-items: center; justify-content: center;
  }

  .step-action {
    position: absolute; left: 0; right: 0; bottom: 0; height: 56px;
    border-top: 1px solid #7a8a96; border-radius: 0 0 8px 8px;
    background: linear-gradient(90deg, var(--btn-light), #2b6fa8 50%, var(--btn-dark));
    color: var(--white); font-size: 16px; letter-spacing: 1px;
    display: flex; align-items: center; justify-content: center;
  }
</style>
</head>
<body>
<main class="page">
  <div class="backdrop" role="img" aria-label="Blurred photograph of tall office buildings against a blue sky"></div>

  <div class="brand">LOGO</div>
  <h1 class="headline">Book your Valuation Online</h1>

  <section class="step step--property">
    <div class="step-tag">STEP 1 of 3</div>
    <h2 class="step-title">PROPERTY DETAILS</h2>
    <div class="step-body">
      <span class="field-label" style="top:18px">POSTAL CODE</span>
      <div class="field-input field-input--short" style="top:46px"></div>
      <div class="search-btn" style="top:46px">SEARCH</div>
      <div class="field-filled" style="top:93px">123 Test Street</div>
      <div class="field-filled" style="top:140px">Test City</div>
      <div class="field-filled" style="top:187px">Test County</div>
    </div>
    <div class="step-action">PROCEED</div>
  </section>

  <section class="step step--details">
    <div class="step-tag">STEP 2 of 3</div>
    <h2 class="step-title">YOUR DETAILS</h2>
    <div class="step-body">
      <span class="field-label" style="top:18px">YOUR NAME</span>
      <div class="field-input" style="top:46px"></div>
      <span class="field-label" style="top:88px">YOUR E-MAIL</span>
      <div class="field-input" style="top:116px"></div>
      <span class="field-label" style="top:158px">YOUR CONTACT NUMBER</span>
      <div class="field-input" style="top:187px"></div>
    </div>
    <div class="step-action">PROCEED</div>
  </section>

  <section class="step step--time">
    <div class="step-tag">STEP 3 of 3</div>
    <h2 class="step-title">APPOINTMENT TIME</h2>
    <div class="step-body">
      <div class="day-toggle day-toggle--today">TODAY</div>
      <div class="day-toggle day-toggle--tomorrow">TOMORROW</div>
      <div class="chip-row chip-row--days">
        <div class="chip">MON<br>30th</div>
        <div class="chip">TUE<br>1st</div>
        <div class="chip">WED<br>2st</div>
        <div class="chip">THURS<br>4th</div>
        <div class="chip">FRI<br>5th</div>
      </div>
      <div class="date-display">Sunday 29 November</div>
      <div class="chip-row chip-row--times">
        <div class="chip">08:30</div>
        <div class="chip chip--selected">10:30</div>
        <div class="chip">12:30</div>
        <div class="chip">14:30</div>
        <div class="chip">16:30</div>
      </div>
    </div>
    <div class="step-action">CONFIRM BOOKING</div>
  </section>
</main>
</body>
</html>
```